High end personal training flyer design

I want a flyer designed to be delivered to people's houses to interest them in high end (and, therefore, not cheap) personal training services.

Don't want standard pictures of people exercising, before and afters, etc. More something that will appeal to that more affluent market.

Flexible on size of flyer, but please make sure it is a standard size that I can get printed easily. Would like it not to look like a normal flyer you get through the letterbox, so if any particular sizes, shapes, etc are known to do that, then that would be a good start.

Text on flyer to be as follows:

Is this you:

Live in East Cheshire
Male, aged 30-50
A father
Cash rich, time poor
Find handling high pressure at work comfortable
But have a short fuse out of work – with the wife, kids, life in general, etc
Not happy with the way your body looks and feels
Know exactly what you should do to sort that, but struggling to actually do it for various reasons
Turned off by the standard menu of options for addressing that – gyms, slimming clubs, diets, etc

If so, you may be interested in what I do.

Some would call it Personal Training. Some would call it Coaching. I’m not interested in giving what I do labels.

What I am interested in is providing the best possible service (and results) for my clients – whatever that entails.

I work closely with one or two clients at a time to make sure they get exactly what they need.

If you would like to find out more about this, I usually meet for a coffee and a chat. To see if we both think our working together is a good idea.

No squeeze pages, no countdowns, mailing lists or false scarcity.

No plastering this flyer with ‘Before and afters’ – they are ten a penny and my clients don’t want to have pictures of them in their underwear spread around the local area.

Just give me a call and we’ll go from there.

My number is 07912645320.

Tim

Industry/Entity Type

Training

Requirements
Should not have
• Generic before and after or exercise type pictures

```html
<!DOCTYPE html>
<html lang="en">
<head>
<meta charset="utf-8">
<title>Personal Training Flyer</title>
<link rel="stylesheet" href="https://fonts.googleapis.com/css2?family=Anton&family=Raleway:ital,wght@0,400;0,700;1,400&display=swap">
<style>
  :root {
    --page-bg: #e9e6e1;
    --flyer-black: #000000;
    --brand-red: #ec1c24;
    --deep-red: #b3141a;
    --text-white: #ffffff;
    --photo-dark: #0a0706;
    --photo-warm: #6b3f2a;
  }
  * { box-sizing: border-box; margin: 0; padding: 0; }
  html, body { width: 900px; height: 1200px; overflow: hidden; }
  body { background: var(--page-bg); position: relative; }

  .flyer {
    position: absolute;
    left: 42px; top: 20px;
    width: 816px; height: 1160px;
    background: var(--flyer-black);
    overflow: hidden;
    color: var(--text-white);
  }

  .hero-photo {
    position: absolute;
    left: 0; top: 0;
    width: 816px; height: 360px;
    background: radial-gradient(ellipse 250px 200px at 50% 45%, var(--photo-warm) 0%, #2a1810 55%, var(--photo-dark) 100%);
  }

  .accent-shapes { position: absolute; left: 0; top: 0; width: 816px; height: 1160px; pointer-events: none; }

  .headline {
    position: absolute;
    left: 28px; top: 360px;
    font-family: "Anton", "Oswald", sans-serif;
    font-weight: 400;
    font-size: 82px;
    line-height: 82px;
    color: var(--brand-red);
    letter-spacing: -0.5px;
    white-space: nowrap;
  }

  .checklist {
    position: absolute;
    left: 28px; top: 472px;
    width: 440px;
    list-style: none;
    font-family: "Raleway", sans-serif;
    font-size: 20.5px;
    line-height: 31.5px;
  }
  .checklist li { position: relative; padding-left: 28px; }
  .checklist .tick {
    position: absolute; left: 0; top: 6px;
    width: 21px; height: 21px;
  }

  .intro-copy {
    position: absolute;
    left: 490px; top: 474px;
    width: 300px;
    font-family: "Raleway", sans-serif;
    font-size: 17px;
    line-height: 22px;
    hyphens: auto;
  }
  .intro-copy p + p { margin-top: 22px; }

  .call-band {
    position: absolute;
    left: 0; top: 982px;
    width: 470px; height: 178px;
  }
  .call-band svg.band-shape { position: absolute; left: 0; top: 0; }
  .call-lead {
    position: absolute; left: 28px; top: 40px;
    font-family: "Raleway", sans-serif; font-weight: 700;
    font-size: 20px; white-space: nowrap;
  }
  .call-prompt {
    position: absolute; left: 28px; top: 76px;
    font-family: "Raleway", sans-serif;
    font-size: 15.5px; text-transform: uppercase; white-space: nowrap;
  }
  .call-number {
    position: absolute; left: 28px; top: 102px;
    display: flex; align-items: center; gap: 10px;
    font-family: "Raleway", sans-serif; font-weight: 700;
    font-size: 34px; white-space: nowrap;
  }
  .call-number .phone-icon { flex: none; width: 33px; height: 33px; }
  .call-number .signature-name { font-weight: 400; font-style: italic; }
</style>
</head>
<body>
  <main class="flyer">
    <div class="hero-photo" role="img" aria-label="Photo of a muscular man with arms raised in triumph against a black background"></div>

    <svg class="accent-shapes" viewBox="0 0 816 1160" aria-hidden="true">
      <polygon points="734,0 816,0 816,76" fill="var(--brand-red)"/>
      <polygon points="768,0 816,0 816,40" fill="var(--deep-red)"/>
      <polygon points="0,126 86,240 86,262 0,218" fill="var(--brand-red)"/>
      <polygon points="0,126 86,240 60,246 0,180" fill="var(--deep-red)"/>
    </svg>

    <h1 class="headline">Is this you:</h1>

    <ul class="checklist">
      <li><svg class="tick" viewBox="0 0 20 20"><circle cx="10" cy="10" r="8.5" fill="none" stroke="#fff" stroke-width="2.2"/><path d="M5.8 10.2l3 3 5.6-6" fill="none" stroke="#fff" stroke-width="2.4"/></svg>Live in East Cheshire</li>
      <li><svg class="tick" viewBox="0 0 20 20"><circle cx="10" cy="10" r="8.5" fill="none" stroke="#fff" stroke-width="2.2"/><path d="M5.8 10.2l3 3 5.6-6" fill="none" stroke="#fff" stroke-width="2.4"/></svg>Male, aged 30-50</li>
      <li><svg class="tick" viewBox="0 0 20 20"><circle cx="10" cy="10" r="8.5" fill="none" stroke="#fff" stroke-width="2.2"/><path d="M5.8 10.2l3 3 5.6-6" fill="none" stroke="#fff" stroke-width="2.4"/></svg>A father</li>
      <li><svg class="tick" viewBox="0 0 20 20"><circle cx="10" cy="10" r="8.5" fill="none" stroke="#fff" stroke-width="2.2"/><path d="M5.8 10.2l3 3 5.6-6" fill="none" stroke="#fff" stroke-width="2.4"/></svg>Cash rich, time poor</li>
      <li><svg class="tick" viewBox="0 0 20 20"><circle cx="10" cy="10" r="8.5" fill="none" stroke="#fff" stroke-width="2.2"/><path d="M5.8 10.2l3 3 5.6-6" fill="none" stroke="#fff" stroke-width="2.4"/></svg>Find handling high pressure at work<br>comfortable</li>
      <li><svg class="tick" viewBox="0 0 20 20"><circle cx="10" cy="10" r="8.5" fill="none" stroke="#fff" stroke-width="2.2"/><path d="M5.8 10.2l3 3 5.6-6" fill="none" stroke="#fff" stroke-width="2.4"/></svg>But have a short fuse out of work<br>– with the wife, kids, life in general, etc</li>
      <li><svg class="tick" viewBox="0 0 20 20"><circle cx="10" cy="10" r="8.5" fill="none" stroke="#fff" stroke-width="2.2"/><path d="M5.8 10.2l3 3 5.6-6" fill="none" stroke="#fff" stroke-width="2.4"/></svg>Not happy with the way your body<br>looks and feels</li>
      <li><svg class="tick" viewBox="0 0 20 20"><circle cx="10" cy="10" r="8.5" fill="none" stroke="#fff" stroke-width="2.2"/><path d="M5.8 10.2l3 3 5.6-6" fill="none" stroke="#fff" stroke-width="2.4"/></svg>Know exactly what you should do<br>to sort that, but struggling to actually<br>do it for various reasons</li>
      <li><svg class="tick" viewBox="0 0 20 20"><circle cx="10" cy="10" r="8.5" fill="none" stroke="#fff" stroke-width="2.2"/><path d="M5.8 10.2l3 3 5.6-6" fill="none" stroke="#fff" stroke-width="2.4"/></svg>Turned off by the standard menu of<br>options for addressing that – gyms,<br>slimming clubs, diets, etc</li>
    </ul>

    <section class="intro-copy">
      <p>Some would call it Personal Training. Some would call it Coaching. I’m not interested in giving what I do labels.</p>
      <p>What I am interested in is providing the best possible service (and results) for my clients – whatever that entails.</p>
      <p>I work closely with one or two clients at a time to make sure they get exactly what they need.</p>
      <p>If you would like to find out more about this, I usually meet for a coffee and a chat. To see if we both think our working together is a good idea.</p>
      <p>No squeeze pages, no countdowns, mailing lists or false scarcity.</p>
      <p>No plastering this flyer with ‘Before and afters’ – they are ten a penny and my clients don’t want to have pictures of them in their underwear spread around the local area.</p>
    </section>

    <section class="call-band">
      <svg class="band-shape" width="470" height="178" viewBox="0 0 470 178" aria-hidden="true">
        <polygon points="0,30 120,18 300,8 420,4 470,12 462,40 470,150 440,168 300,172 0,178" fill="var(--brand-red)"/>
      </svg>
      <p class="call-lead">If so, you may be interested in what I do.</p>
      <p class="call-prompt">Just give me a call and we’ll go from there.</p>
      <p class="call-number">
        <svg class="phone-icon" viewBox="0 0 32 32" aria-hidden="true"><circle cx="16" cy="16" r="16" fill="#000"/><path d="M11.2 8.5l2.4-.6 1.6 4.1-1.8 1.4c.9 2 2.4 3.5 4.3 4.4l1.4-1.8 4.1 1.6-.6 2.4c-.2.8-1 1.3-1.8 1.2-5.4-.7-9.6-4.9-10.3-10.3-.1-.8.4-1.5 1.2-1.8z" fill="#fff"/></svg>
        <span>07912645320 - <span class="signature-name">Tim</span></span>
      </p>
    </section>
  </main>
</body>
</html>
```